Business Card Design Project

I require a business card design that looks professional for a small building company. Calloway Builders is the name of the company and i don't want to use a house or building design for a logo. I require a logo design for the card incorporating the name Calloway Builders but designed smartly.

We are a Registered Building Practitioner so the small logo attached must also be used on the card.

We cover a large range of Building / Construction, Concrete, Steelwork. Not sure how to implement this.

Colors are flexible, maybe a dark grey background with white writting over it, but i am keen to see other options.

Thanks.

Target Market(s)

Anyone

Industry/Entity Type

Building

Requirements
Must have
• The logo attached must be incorporated - can be small
A logo for my company needs to be included - using Calloway Builders as the base with no picture of a house or buildings.

```html
<!DOCTYPE html>
<html lang="en">
<head>
<meta charset="utf-8">
<title>Calloway Builders — Business Card</title>
<link rel="stylesheet" href="https://fonts.googleapis.com/css2?family=Fira+Sans:wght@400;500;600&display=swap">
<style>
  :root {
    --backdrop: #2b2b2b;
    --brand-red: #7a1114;
    --brand-red-light: #9e1a1f;
    --brand-red-deep: #4e0406;
    --brand-orange: #f39a1e;
    --paper: #ffffff;
    --badge-blue: #1f3f7a;
    --badge-grey: #c9ced8;
  }
  * { margin: 0; padding: 0; box-sizing: border-box; }
  html, body { width: 1200px; height: 900px; overflow: hidden; }
  body {
    background: var(--backdrop);
    font-family: "Fira Sans", Arial, sans-serif;
    position: relative;
  }
  .card {
    position: absolute;
    width: 540px;
    height: 310px;
    box-shadow: 0 12px 30px rgba(0,0,0,0.45);
    overflow: hidden;
  }
  /* Front */
  .card-front {
    left: 60px;
    top: 140px;
    background: radial-gradient(circle at 30% 22%, var(--brand-red-light) 0%, var(--brand-red) 38%, var(--brand-red-deep) 100%);
  }
  .front-brand {
    position: absolute;
    left: 0; right: 0; top: 118px;
    display: flex;
    justify-content: center;
    align-items: center;
    gap: 12px;
  }
  .brand-square {
    width: 22px; height: 22px;
    background: var(--brand-orange);
  }
  .brand-name {
    color: var(--brand-orange);
    font-weight: 600;
    font-size: 30px;
    letter-spacing: 0.2px;
  }
  .front-web {
    position: absolute;
    left: 0; right: 0; bottom: 36px;
    text-align: center;
    color: var(--paper);
    font-weight: 500;
    font-size: 14px;
  }
  /* Back */
  .card-back {
    left: 600px;
    top: 430px;
    background: var(--brand-red);
  }
  .back-band {
    position: absolute;
    left: 60px; top: 0;
    width: 200px; height: 100%;
    background: var(--paper);
  }
  .band-brand {
    position: absolute;
    left: 0; right: 0; top: 118px;
    display: flex;
    flex-direction: column;
    align-items: center;
    gap: 10px;
  }
  .band-brand .brand-square { width: 20px; height: 20px; }
  .band-brand .brand-name { font-size: 21px; }
  .registration-badge {
    position: absolute;
    left: 18px; bottom: 22px;
    display: flex;
    align-items: center;
    gap: 8px;
  }
  .badge-seal {
    width: 34px; height: 34px;
    border-radius: 50%;
    border: 3px solid var(--badge-blue);
    background: var(--badge-grey);
  }
  .badge-plate {
    width: 118px; height: 24px;
    background: var(--badge-blue);
    border-radius: 3px;
  }
  .contact {
    position: absolute;
    left: 302px; top: 46px;
    color: var(--paper);
  }
  .contact-name { font-size: 20px; font-weight: 600; }
  .contact-role { color: var(--brand-orange); font-size: 14px; font-weight: 600; margin-top: 1px; }
  .contact-address { font-size: 12.5px; font-weight: 500; line-height: 1.35; margin-top: 30px; }
  .contact-lines {
    display: grid;
    grid-template-columns: 66px auto;
    row-gap: 2px;
    margin-top: 18px;
    font-size: 12.5px;
    font-weight: 500;
  }
  .contact-label { color: var(--brand-orange); font-weight: 600; }
</style>
</head>
<body>
  <section class="card card-front" aria-label="Business card front">
    <div class="front-brand">
      <span class="brand-square"></span>
      <span class="brand-name">Calloway Builders</span>
    </div>
    <p class="front-web">www.callowaybuilders.com</p>
  </section>

  <section class="card card-back" aria-label="Business card back">
    <div class="back-band">
      <div class="band-brand">
        <span class="brand-square"></span>
        <span class="brand-name">Calloway Builders</span>
      </div>
      <div class="registration-badge" role="img" aria-label="Registered building practitioner badge">
        <span class="badge-seal"></span>
        <span class="badge-plate"></span>
      </div>
    </div>
    <div class="contact">
      <p class="contact-name">Daniel Harper</p>
      <p class="contact-role">Director</p>
      <p class="contact-address">2140 Ridgeline Court,<br>Fairmont, CA 94512</p>
      <div class="contact-lines">
        <span class="contact-label">Phone:</span><span>555 204 3187</span>
        <span class="contact-label">Email:</span><span>dharper@cbcompany.com</span>
        <span class="contact-label">Website:</span><span>www.callowaybuilders.com</span>
      </div>
    </div>
  </section>
</body>
</html>
```